Meridian Rest Supply Needs Business Card

Looking for a very nice looking business card. Creative but not extravagant. We sell beds and pillows across the U.S. and need something professional but catchy. I have attached the logo.

Name : Dale Fenwick
Title : President
Phone : (800) 417-2964
Email: sleep@quorvana.com
Website: www.quorvana.com

Can be single-sided or double-sided
horizontal or vertical

Can use Blues/Greys

Target Market(s)

Mass Market

Industry/Entity Type

Retail

Contact Information for Business Card

Name : Dale Fenwick
Title : President
Phone : (800) 417-2964
Email: sleep@quorvana.com
Website: www.quorvana.com

Requirements
Must have
• Clean, Modern, Smooth
• Can use Blues/Greys
• On the other side without the information - have something simple like www.quorvana.com or our logo
Nice to have
• Surprise me
Should not have
• Nothing crazy, nothing cluttered

```html
<!DOCTYPE html>
<html lang="en">
<head>
<meta charset="utf-8">
<title>Meridian Rest Supply – Business Card</title>
<link rel="stylesheet" href="https://fonts.googleapis.com/css2?family=Montserrat:wght@300;400;700&display=swap">
<style>
  :root {
    --backdrop: #a6b1bc;
    --card: #d4dae0;
    --brand-blue: #36a3d6;
    --brand-blue-soft: #5bb5df;
  }
  html, body {
    margin: 0;
    padding: 0;
    width: 1200px;
    height: 1200px;
    overflow: hidden;
    background: var(--backdrop);
    font-family: "Montserrat", sans-serif;
  }
  .canvas {
    position: relative;
    width: 1200px;
    height: 1200px;
  }
  .card {
    position: absolute;
    width: 780px;
    height: 443px;
    background: var(--card);
    color: var(--brand-blue);
  }
  .card-front { left: 205px; top: 124px; }
  .card-back  { left: 211px; top: 649px; }

  .brand-name {
    position: absolute;
    inset: 0;
    display: flex;
    align-items: center;
    justify-content: center;
    margin: 0;
    font-weight: 300;
    font-size: 92px;
    letter-spacing: 3px;
    color: var(--brand-blue);
  }

  .identity {
    position: absolute;
    left: 0;
    width: 388px;
    top: 155px;
    text-align center;
    text-align: center;
  }
  .person-name {
    margin: 0;
    font-size: 50px;
    font-weight: 400;
    line-height: 1;
  }
  .person-name strong { font-weight: 700; }
  .person-title {
    margin: 10px 0 0;
    font-size: 39px;
    font-weight: 400;
    letter-spacing: 1px;
    line-height: 1;
  }

  .contact-illustration {
    position: absolute;
    left: 379px;
    top: 90px;
    width: 123px;
    height: 310px;
    border-radius: 6px;
    background: linear-gradient(180deg, var(--brand-blue) 0%, var(--brand-blue-soft) 50%, var(--brand-blue) 100%);
  }

  .contact-list {
    position: absolute;
    left: 514px;
    top: 0;
    margin: 0;
    padding: 0;
    list-style: none;
    font-size: 16px;
    font-weight: 400;
    line-height: 20px;
  }
  .contact-list li { position: absolute; left: 0; white-space: nowrap; }
  .contact-email   { top: 117px; }
  .contact-phone   { top: 193px; }
  .contact-address { top: 258px; }
  .contact-web     { top: 342px; }
</style>
</head>
<body>
<main class="canvas">
  <section class="card card-front" aria-label="Card front">
    <h1 class="brand-name">quorvana</h1>
  </section>

  <section class="card card-back" aria-label="Card back">
    <div class="identity">
      <p class="person-name">Dale <strong>Fenwick</strong></p>
      <p class="person-title">PRESIDENT</p>
    </div>

    <div class="contact-illustration" role="img" aria-label="Stacked illustration of an envelope, telephone handset, house and globe"></div>

    <ul class="contact-list">
      <li class="contact-email">sleep@quorvana.com</li>
      <li class="contact-phone">(800) 417-2964</li>
      <li class="contact-address">Your City Address<br>Street Location, NY City, USA</li>
      <li class="contact-web">www.quorvana.com</li>
    </ul>
  </section>
</main>
</body>
</html>
```